VORDA HOMES PELAB MARKETING FLYER

THE FLYER CAN BE FRONT TO BACK OR 2 PAGES IF NEEDED.

need to create a flyer with the following information:

Tallyworth Inc. is a CRM (Customer Relationship Management System) that provides leads to agents and a system to communicate and track your leads. Initial training and set up will be provided

Commission splits for leads are as follows: (maybe we can create a chart or box for items 1-3)

1. Cold leads 40% Vorda - 60% Agent - Worked by Agent in the platform, agent shows property, writes contract, handles all negotiations and any necessary addendums, attends home inspection and settlement.

2. Warm leads 50% Vorda - 50% Co-agent - Contacted by ISA, agent shows property, writes contract, handles all negotiations and any necessary addendums, attends home inspection and settlement.

3 Hot leads 70% Vorda - 30% Co-agent - Prequalified by Vorda Homes and ready to look at property, Vorda writes contract and secures broker agency relationship agreements, co-agent shows property, , handles all negotiations (with support from VORDA if necessary), execute any necessary addendums, attend home inspection and settlement.

Preferred vendors such as Lender, Title, Insurance, Home Inspector, etc. are to be used for any transactions related to PELB per Vorda Homes.

Agents will receive 10 leads for free to start once Fresh Broker Launchpad is complete. Warm leads will be available to purchase for $15 each beyond the first 10. Every 5 deals closed, agent commission will increase by 10% annually!!

Rules and restrictions apply.

3. In addition to Quillset, a transaction coordinator included.

4. Free PELB Support and training included

5. Free personal CRM website included

Industry/Entity Type

Real Estate

Colors
3176b5
85abd2
ecf5f6

Requirements
Must have
• everything in the description above

```html
<!DOCTYPE html>
<html lang="en">
<head>
<meta charset="UTF-8">
<title>Vorda Homes · PELB Marketing Flyer</title>
<link href="https://fonts.googleapis.com/css2?family=Roboto:wght@400;500;700&display=swap" rel="stylesheet">
<style>
  :root {
    --navy: #0d4595;
    --gold: #f9c851;
    --ink: #1f2a3a;
    --paper: #ffffff;
    --page-bg: #ecf5f6;
    --sky-top: #3a7fd0;
    --sky-mid: #9cc4ea;
    --lawn: #4f8a22;
  }
  * { box-sizing: border-box; margin: 0; padding: 0; }
  html, body { width: 747px; height: 1200px; overflow: hidden; background: var(--page-bg); }
  body { font-family: "Roboto", Arial, sans-serif; color: var(--ink); }

  .flyer { position: relative; width: 747px; height: 1200px; background: var(--paper); overflow: hidden; }

  .top-band { position: absolute; left: 0; top: 0; width: 100%; height: 18px; background: var(--navy); }

  .brand { position: absolute; display: flex; align-items: center; gap: 8px; color: var(--navy); font-weight: 500; white-space: nowrap; }
  .brand-main { left: 47px; top: 62px; font-size: 28px; letter-spacing: 1px; }
  .brand-main .mark { width: 34px; height: 34px; background: var(--navy); }
  .brand-partner { left: 470px; top: 74px; font-size: 26px; letter-spacing: 1px; }
  .brand-partner .mark { width: 12px; height: 12px; border-radius: 50%; background: var(--navy); }
  .brand-group { left: 610px; top: 76px; font-size: 10px; font-weight: 400; width: 110px; line-height: 1.3; text-align: center; display: block; white-space: normal; }

  .hero { position: absolute; left: 0; top: 149px; width: 100%; height: 401px;
    background: linear-gradient(180deg, var(--sky-top) 0%, var(--sky-mid) 40%, #cfd8d6 55%, #6f9a3a 72%, var(--lawn) 100%); }

  .intro { position: absolute; left: 62px; top: 566px; width: 630px; font-size: 12.5px; line-height: 1.5; }

  .section-head { position: absolute; left: 0; top: 630px; width: 452px; height: 50px; }
  .section-head svg { position: absolute; inset: 0; }
  .section-head h2 { position: relative; color: #fff; font-size: 18px; font-weight: 500; line-height: 50px; padding-left: 39px; white-space: nowrap; }

  .split { position: absolute; left: 61px; font-size: 12px; line-height: 1.5; font-weight: 500; text-align: justify; padding: 10px 20px 10px 21px; }
  .split.gold { background: var(--gold); color: var(--navy); width: 577px; }
  .split.navy { background: var(--navy); color: #fff; width: 636px; }
  .split-1 { top: 700px; height: 80px; padding-top: 13px; }
  .split-2 { top: 784px; height: 62px; padding-top: 13px; }
  .split-3 { top: 849px; height: 101px; padding-top: 12px; }
  .step { position: absolute; left: 38px; width: 25px; height: 25px; border-radius: 50%; background: #fff; border: 1.5px solid var(--navy);
    color: var(--navy); font-size: 11px; font-weight: 500; display: flex; align-items: center; justify-content: center; z-index: 2; }

  .notes-bar { position: absolute; left: 61px; top: 950px; width: 36px; height: 112px; background: var(--navy); }
  .notes { position: absolute; left: 117px; top: 968px; width: 522px; font-size: 12px; line-height: 1.5; text-align: justify; }
  .notes p + p { margin-top: 10px; }

  .perks { position: absolute; left: 61px; top: 1074px; width: 390px; height: 77px; background: var(--gold); padding: 9px 0 0 10px; list-style: none; }
  .perks li { display: flex; align-items: center; gap: 14px; color: var(--navy); font-size: 12px; font-weight: 500; line-height: 20px; white-space: nowrap; }
  .perks li::before { content: ""; width: 9px; height: 9px; background: var(--navy); flex: none; }

  .rules { position: absolute; left: 497px; top: 1083px; width: 216px; text-align: center; color: var(--navy); font-weight: 700; }
  .rules .label { background: var(--gold); font-size: 14px; line-height: 33px; }
  .rules .tail { font-size: 18px; margin-top: 8px; }

  .foot { position: absolute; left: 0; bottom: 0; width: 100%; height: 18px; }
</style>
</head>
<body>
<main class="flyer">
  <div class="top-band"></div>

  <div class="brand brand-main"><span class="mark"></span>VORDA HOMES</div>
  <div class="brand brand-partner"><span class="mark"></span>PELB</div>
  <div class="brand brand-group">Meridale Property Group</div>

  <div class="hero" role="img" aria-label="Photo of a white two-gabled family house on a sunny green lawn under blue sky"></div>

  <p class="intro">Tallyworth Inc. is a CRM (Customer Relationship Management System) that provides leads to agents and a system to communicate and track your leads. Initial training and set up will be provided</p>

  <div class="section-head">
    <svg width="452" height="50" viewBox="0 0 452 50"><polygon points="0,0 434,0 452,50 0,50" fill="#0d4595"/></svg>
    <h2>Commission splits for leads are as follows:</h2>
  </div>

  <span class="step" style="top:688px">1</span>
  <div class="split gold split-1">Cold leads 40% Vorda - 60% Agent - Worked by Agent in the platform, agent shows property, writes contract, handles all negotiations and any necessary addendums, attends home inspection and settlement</div>

  <span class="step" style="top:772px">2</span>
  <div class="split navy split-2">Warm leads 50% Vorda - 50% Co-agent - Contacted by ISA, agent shows property, writes contract, handles all negotiations and any necessary addendums, attends home inspection and settlement.</div>

  <span class="step" style="top:837px">3</span>
  <div class="split gold split-3">Hot leads 70% Vorda - 30% Co-agent - Prequalified by Vorda Homes and ready to look at property, Vorda writes contract and secures broker agency relationship agreements, co-agent shows property, handles all negotiations (with support from VORDA if necessary), execute any necessary addendums, attend home inspection and settlement.</div>

  <div class="notes-bar"></div>
  <div class="notes">
    <p>Preferred vendors such as Lender, Title, Insurance, Home Inspector, etc. are to be used for any transactions related to PELB per Vorda Homes</p>
    <p>Agents will receive 10 leads for free to start once Fresh Broker Launchpad is complete. Warm leads will be available to purchase for $15 each beyond the first 10. Every 5 deals closed, agent commission will increase by 10% annually!!</p>
  </div>

  <ul class="perks">
    <li>In addition to Quillset, a transaction coordinator included.</li>
    <li>Free PELB Support and training included</li>
    <li>Free personal CRM website included</li>
  </ul>

  <div class="rules">
    <div class="label">RULES AND RESTRICTIONS</div>
    <div class="tail">WILL APPLY</div>
  </div>

  <svg class="foot" width="747" height="18" viewBox="0 0 747 18">
    <polygon points="0,0 497,0 515,18 0,18" fill="#0d4595"/>
    <polygon points="506,0 747,0 747,18 524,18" fill="#f9c851"/>
  </svg>
</main>
</body>
</html>
```